Accounting and Financial Services Firm - Modern, Fresh, Original, Professional

We need a business card designed. We would like to see use of the the colors blue. Logo attached.

Modern, Fresh, Original, Professional,
Updates

Email section on business card required. design brief updated.

Target Market(s)

Small to medium businesses and high net worth individuals

Industry/Entity Type

Public Accounting

Contact Information for Business Card

Business Name: PL Ledgerworth Chartered Accountants
Address: Level 9, 42 Garnet Lane Sydney NSW 2000
Ph: 02 9314 2758
Mobile: 04 XXXX XXXX
Email: mara@plledgerworth.com.au
Wechat ID: XXXXXXX
Website: www.plledgerworth.com.au

Name: Mara Osei
Position: Manager

Font styles to use
Sans Serif

Colors
0492cd
33a6d7
85cae6

Requirements
Must have
• Modern font.

```html
<!DOCTYPE html>
<html lang="en">
<head>
<meta charset="utf-8">
<title>PL Ledgerworth Chartered Accountants – Business Card</title>
<link href="https://fonts.googleapis.com/css2?family=Josefin+Sans:wght@300;400&family=Open+Sans:wght@400&display=swap" rel="stylesheet">
<style>
  :root {
    --blue-deep: #0492cd;
    --blue-mid: #33a6d7;
    --blue-light: #85cae6;
    --card-black: #060708;
    --band-grey: #8f9194;
    --text-grey: #9a9da1;
    --page: #e9eaec;
  }
  * { margin: 0; padding: 0; box-sizing: border-box; }
  html, body { width: 1200px; height: 1200px; overflow: hidden; }
  body {
    background: var(--page);
    position: relative;
    font-family: "Open Sans", sans-serif;
  }
  .card {
    position: absolute;
    left: 190px;
    width: 820px;
    height: 500px;
    background: var(--card-black);
    box-shadow: 0 8px 24px rgba(0,0,0,0.18);
    overflow: hidden;
  }
  .card--front { top: 60px; }
  .card--back { top: 630px; }

  .wordmark {
    font-family: "Josefin Sans", sans-serif;
    font-weight: 400;
    color: var(--blue-deep);
    text-transform: uppercase;
    line-height: 1.15;
  }
  .card--front .wordmark {
    position: absolute;
    inset: 0;
    display: flex;
    flex-direction: column;
    align-items: center;
    justify-content: center;
    text-align: center;
  }
  .card--front .wordmark__name { font-size: 50px; letter-spacing: 3px; }
  .card--front .wordmark__sub { font-size: 17px; letter-spacing: 4px; margin-top: 6px; }

  .card--back .wordmark {
    position: absolute;
    right: 70px;
    top: 62px;
    text-align: right;
  }
  .card--back .wordmark__name { font-size: 36px; letter-spacing: 2px; }
  .card--back .wordmark__sub { font-size: 12px; letter-spacing: 3px; margin-top: 4px; }

  .person {
    position: absolute;
    left: 60px;
    top: 212px;
    display: flex;
    align-items: baseline;
    gap: 14px;
  }
  .person__name {
    font-family: "Josefin Sans", sans-serif;
    font-weight: 400;
    font-size: 34px;
    color: var(--blue-deep);
    text-transform: uppercase;
    letter-spacing: 1px;
  }
  .person__divider { width: 2px; height: 30px; background: var(--blue-deep); align-self: center; }
  .person__role { font-size: 16px; color: var(--text-grey); }

  .rule {
    position: absolute;
    left: 60px;
    right: 70px;
    top: 300px;
    height: 1px;
    background: var(--blue-deep);
  }

  .contact {
    position: absolute;
    left: 60px;
    font-size: 18px;
    line-height: 26px;
    color: var(--text-grey);
    display: flex;
    align-items: center;
    gap: 10px;
  }
  .contact svg { width: 18px; height: 18px; fill: var(--blue-deep); flex: none; }
  .contact--address { top: 262px; }
  .contact--mobile { top: 314px; }
  .contact--phone { top: 344px; }
  .contact--email { top: 374px; }
  .contact--web { top: 404px; }

  .messenger {
    position: absolute;
    right: 70px;
    top: 262px;
    font-size: 18px;
    line-height: 26px;
    color: var(--text-grey);
    display: flex;
    align-items: center;
    gap: 10px;
  }
  .messenger__dot { width: 16px; height: 16px; border-radius: 50%; background: var(--blue-mid); }

  .band {
    position: absolute;
    left: 0; right: 0; bottom: 0;
    height: 46px;
    background: var(--band-grey);
  }
</style>
</head>
<body>

<section class="card card--front" aria-label="Card front">
  <div class="wordmark">
    <span class="wordmark__name">PL Ledgerworth</span>
    <span class="wordmark__sub">Chartered Accountants</span>
  </div>
</section>

<section class="card card--back" aria-label="Card back">
  <div class="wordmark">
    <div class="wordmark__name">PL Ledgerworth</div>
    <div class="wordmark__sub">Chartered Accountants</div>
  </div>

  <div class="person">
    <span class="person__name">Mara Osei</span>
    <span class="person__divider"></span>
    <span class="person__role">Manager</span>
  </div>

  <div class="contact contact--address">
    <svg viewBox="0 0 24 24"><path d="M12 2a7 7 0 0 0-7 7c0 5 7 13 7 13s7-8 7-13a7 7 0 0 0-7-7zm0 9.5A2.5 2.5 0 1 1 12 6.5a2.5 2.5 0 0 1 0 5z"/></svg>
    <span>Level 9, 42 Garnet Lane, Sydney NSW 2000</span>
  </div>

  <div class="messenger"><span>XXXXXXX</span><span class="messenger__dot"></span></div>

  <div class="rule"></div>

  <div class="contact contact--mobile">
    <svg viewBox="0 0 24 24"><path d="M7 2h10a1 1 0 0 1 1 1v18a1 1 0 0 1-1 1H7a1 1 0 0 1-1-1V3a1 1 0 0 1 1-1zm1 3v12h8V5H8zm4 13.5a1 1 0 1 0 0 2 1 1 0 0 0 0-2z"/></svg>
    <span>04 XXXX XXXX</span>
  </div>
  <div class="contact contact--phone">
    <svg viewBox="0 0 24 24"><path d="M6.6 10.8a15 15 0 0 0 6.6 6.6l2.2-2.2a1 1 0 0 1 1-.25 11.4 11.4 0 0 0 3.6.57 1 1 0 0 1 1 1V20a1 1 0 0 1-1 1A17 17 0 0 1 3 4a1 1 0 0 1 1-1h3.5a1 1 0 0 1 1 1c0 1.25.2 2.45.57 3.57a1 1 0 0 1-.25 1z"/></svg>
    <span>02 9314 2758</span>
  </div>
  <div class="contact contact--email">
    <svg viewBox="0 0 24 24"><path d="M3 5h18a1 1 0 0 1 1 1v12a1 1 0 0 1-1 1H3a1 1 0 0 1-1-1V6a1 1 0 0 1 1-1zm1 2.3V17h16V7.3l-8 5.4-8-5.4zM5.2 7 12 11.5 18.8 7H5.2z"/></svg>
    <span>mara@plledgerworth.com.au</span>
  </div>
  <div class="contact contact--web">
    <svg viewBox="0 0 24 24"><path d="M12 2a10 10 0 1 0 0 20 10 10 0 0 0 0-20zm6.9 6h-2.9a15.7 15.7 0 0 0-1.4-3.6A8 8 0 0 1 18.9 8zM12 4c.8 1.2 1.5 2.5 1.9 4h-3.8c.4-1.5 1.1-2.8 1.9-4zM4.3 14a8 8 0 0 1 0-4h3.4a16 16 0 0 0 0 4H4.3zm.8 2h2.9c.3 1.3.8 2.5 1.4 3.6A8 8 0 0 1 5.1 16zM8 8H5.1a8 8 0 0 1 4.3-3.6C8.8 5.5 8.3 6.7 8 8zm4 12c-.8-1.2-1.5-2.5-1.9-4h3.8c-.4 1.5-1.1 2.8-1.9 4zm2.3-6H9.7a14.7 14.7 0 0 1 0-4h4.6a14.7 14.7 0 0 1 0 4zm.3 5.6c.6-1.1 1.1-2.3 1.4-3.6h2.9a8 8 0 0 1-4.3 3.6zM16.3 14a16 16 0 0 0 0-4h3.4a8 8 0 0 1 0 4h-3.4z"/></svg>
    <span>www.plledgerworth.com.au</span>
  </div>

  <div class="band"></div>
</section>

</body>
</html>
```